Label for natural soft drink / juice

Required is a label design that adds a frame for a range of different labels linked to a variety of tastes for a natural, organic, sparkling beverage in a multi-use, environmentally friendly returnable clear glass bottle.
The 2 first tastes are rhubarb and apple
The label will be a paper label sticked at the front side of the bottle.
No glossy or shiny appearance as it does not fit the organic image
No color restrictions in general, but
Blue better than green
Matt better than glossy
Fit of colours on one label essential, so no “crying colour mixture” (great also: complementary contrasts like blue/orange)
Handpainted better than photorealistic
Simple better than overcrowded
Smart, funny intelligent a lot better than same standard as everywhere
For the image consider subtile reminiscence to the fruit or other stuff linked to the fruit (even “across 3 corners”, so a bit far away) as a nice additional asset

Target Market(s)

modern restaurants with high quality food, often with organic and regional products on the menu.

Font styles to use
Serif
Sans Serif
Script

Requirements
Nice to have
• the fruit of the current taste or something linked to the fruit as e.g. reminiscence to well known story or history of the fruit
Should not have
• too many elements on the label. simplicity is key

```html
<!DOCTYPE html>
<html lang="en">
<head>
<meta charset="utf-8">
<title>Freshly Made Apple Juice – Label</title>
<link href="https://fonts.googleapis.com/css2?family=Montserrat:wght@300;400;700;800&display=swap" rel="stylesheet">
<style>
  :root {
    --bg: #a3283a;
    --paper: #f2f1ef;
    --kraft: #b89c7b;
    --ink: #1c2236;
    --sun: #e6cc2c;
    --tag: #1a1a1a;
    --tag-text: #f4f4f4;
  }
  * { margin: 0; padding: 0; box-sizing: border-box; }
  html, body {
    width: 1200px; height: 1000px; overflow: hidden;
    background: var(--bg);
    font-family: "Montserrat", sans-serif;
    color: var(--ink);
  }
  .canvas { position: relative; width: 1200px; height: 1000px; }
  .label {
    position: absolute; left: 140px; top: 220px;
    width: 920px; height: 420px;
    display: flex; flex-direction: column;
  }
  .label__front {
    position: relative;
    height: 210px; background: var(--paper);
    padding: 0 0 0 300px;
    display: flex; flex-direction: column; justify-content: center;
  }
  .label__back { position: relative; flex: 1; background: var(--kraft); }
  .volume {
    position: absolute; left: 22px; top: 50%;
    transform: translateY(-50%) rotate(-90deg);
    font-size: 17px; font-weight: 400; letter-spacing: .5px;
  }
  .sun-disc {
    position: absolute; left: 80px; top: 110px;
    width: 190px; height: 190px; border-radius: 50%;
    background: var(--sun);
  }
  .fruit-art {
    position: absolute; left: 95px; top: 40px;
    width: 150px; height: 140px;
  }
  .title__kicker { font-size: 34px; font-weight: 300; line-height: 1; }
  .title__main {
    font-size: 58px; font-weight: 800; line-height: 1.05; letter-spacing: -.5px;
  }
  .facts {
    position: absolute; left: 300px; top: 26px; width: 290px;
    font-size: 20px; font-weight: 400; line-height: 1.35;
  }
  .facts__head {
    padding-bottom: 6px; margin-bottom: 6px;
    border-bottom: 1.5px solid var(--ink);
  }
  .maker {
    position: absolute; right: 40px; top: 50%;
    transform: translateY(-50%);
    display: flex; align-items: center; gap: 14px;
    white-space: nowrap;
  }
  .maker__dot { width: 30px; height: 30px; border-radius: 50%; background: var(--ink); }
  .maker__name {
    font-size: 24px; font-weight: 700; letter-spacing: 2px; text-transform: uppercase;
  }
  .neck-tag {
    position: absolute; left: 360px; top: 760px;
    width: 480px; height: 62px; background: var(--tag);
    display: flex; align-items: center; justify-content: center;
    color: var(--tag-text); font-size: 26px; font-weight: 400; letter-spacing: 2px;
  }
</style>
</head>
<body>
<main class="canvas">
  <section class="label">
    <div class="label__front">
      <span class="volume">200 ml</span>
      <p class="title__kicker">freshly made</p>
      <h1 class="title__main">apple juice</h1>
    </div>
    <div class="label__back">
      <div class="facts">
        <p class="facts__head">Ingredients list here</p>
        <p>No Added Sugar</p>
        <p>No Added Water</p>
        <p>No Preservatives</p>
      </div>
      <div class="maker">
        <span class="maker__dot"></span>
        <span class="maker__name">Orchard Row</span>
      </div>
    </div>
    <div class="sun-disc"></div>
    <svg class="fruit-art" role="img" aria-label="Watercolour red apple with leaf and a cut slice" viewBox="0 0 150 140">
      <defs>
        <radialGradient id="appleTone" cx="40%" cy="40%" r="65%">
          <stop offset="0" stop-color="#c8323e"/>
          <stop offset="1" stop-color="#7e1020"/>
        </radialGradient>
      </defs>
      <rect x="0" y="10" width="150" height="130" rx="60" fill="url(#appleTone)"/>
    </svg>
  </section>
  <div class="neck-tag">freshly made with love</div>
</main>
</body>
</html>
```